ashby paving works

Needs to have phone number 0412885107 and email marklowry@pavemail.com.au.
ABN 27613048852
name mark lowry

For all your concreting solutions
Excavation
Exposed & colour concrete
House & shed slabs
Driveways
Landing & steps

Contact Information for Business Card

ph 0412885107
email marklowry@pavemail.com.au.
ABN 27613048852
name mark lowry

```html
<!DOCTYPE html>
<html lang="en">
<head>
<meta charset="utf-8">
<title>Ashby Paving Works – Business Cards</title>
<link href="https://fonts.googleapis.com/css2?family=Lato:wght@400;700;900&display=swap" rel="stylesheet">
<style>
  :root {
    --orange: #f26a22;
    --orange-deep: #e85a1a;
    --orange-light: #f47a2a;
    --grey: #5a5a5a;
    --grey-text: #6b6b6b;
    --white: #ffffff;
    --backdrop: #3a3a3a;
    --backdrop-edge: #1f1f1f;
  }
  * { margin: 0; padding: 0; box-sizing: border-box; }
  html, body {
    width: 1200px; height: 900px; overflow: hidden;
    font-family: "Lato", sans-serif;
  }
  body {
    background: radial-gradient(ellipse at 50% 45%, var(--backdrop) 0%, var(--backdrop-edge) 100%);
    position: relative;
  }
  .card {
    position: absolute;
    width: 540px; height: 309px;
    overflow: hidden;
    box-shadow: 0 14px 30px rgba(0,0,0,0.45);
  }

  /* ---------- Front card ---------- */
  .card-front { left: 40px; top: 296px; background: var(--white); }
  .card-front .art { position: absolute; inset: 0; }
  .person { position: absolute; left: 30px; top: 28px; }
  .person-name {
    color: var(--orange); font-weight: 900; font-size: 26px;
    letter-spacing: 0.5px; text-transform: uppercase;
  }
  .person-role { color: var(--grey-text); font-size: 13px; margin-top: 2px; }

  .company-block {
    position: absolute; right: 26px; top: 34px; text-align: right; width: 250px;
  }
  .company-name {
    color: var(--orange); font-weight: 700; font-size: 17px;
    letter-spacing: 1.5px; text-transform: uppercase;
  }
  .company-rule { height: 1px; background: var(--grey); margin: 6px 0 6px 40px; }
  .company-phone {
    color: var(--orange); font-size: 15px; letter-spacing: 3px; padding-right: 40px;
  }

  .contact {
    position: absolute; left: 30px; top: 166px;
    color: var(--white); font-size: 12.5px; line-height: 1.5;
    list-style: none;
  }
  .contact li { display: flex; align-items: center; gap: 7px; }
  .contact svg { width: 11px; height: 11px; flex: none; }
  .contact .abn-label { font-weight: 700; }

  /* ---------- Back card ---------- */
  .card-back {
    left: 620px; top: 296px;
    background: linear-gradient(135deg, var(--orange-deep) 0%, var(--orange-light) 55%, var(--orange-deep) 100%);
  }
  .brand {
    position: absolute; left: 108px; top: 56px;
    display: flex; align-items: center; gap: 22px;
  }
  .brand-mark { width: 62px; height: 62px; background: var(--white); }
  .brand-divider { width: 1px; height: 96px; background: var(--white); }
  .brand-text { color: var(--white); }
  .brand-name {
    font-weight: 700; font-size: 19px; letter-spacing: 1.5px; text-transform: uppercase;
  }
  .brand-rule { height: 1px; background: var(--white); margin: 6px 0; width: 100%; }
  .brand-phone { font-size: 15px; letter-spacing: 3px; }

  .services {
    position: absolute; left: 108px; right: 40px; top: 186px;
    color: var(--white);
  }
  .services-tagline { font-size: 13px; font-weight: 700; letter-spacing: 0.3px; margin-bottom: 5px; }
  .services-list {
    list-style: none; display: flex; flex-wrap: wrap;
    font-size: 11.5px; line-height: 1.6;
  }
  .services-list li:not(:last-child)::after { content: "·"; margin: 0 6px; }

  .web {
    position: absolute; left: 108px; bottom: 26px;
    color: var(--white); font-size: 13px; letter-spacing: 0.3px;
  }
</style>
</head>
<body>

<section class="card card-front" aria-label="Business card front">
  <svg class="art" width="540" height="309" viewBox="0 0 540 309" aria-hidden="true">
    <defs>
      <linearGradient id="bandGrad" x1="0" y1="0" x2="1" y2="1">
        <stop offset="0" stop-color="#f47a2a"/>
        <stop offset="1" stop-color="#e85a1a"/>
      </linearGradient>
    </defs>
    <polygon points="0,150 340,150 450,309 0,309" fill="url(#bandGrad)"/>
    <polygon points="340,150 540,150 540,309 450,309" fill="#ffffff"/>
    <polygon points="395,228 540,200 540,309 450,309" fill="#5a5a5a"/>
    <rect x="405" y="222" width="62" height="62" fill="#ffffff"/>
  </svg>

  <div class="person">
    <h1 class="person-name">Mark Lowry</h1>
    <p class="person-role">Director</p>
  </div>

  <div class="company-block">
    <p class="company-name">Ashby Paving Works</p>
    <div class="company-rule"></div>
    <p class="company-phone">0412885107</p>
  </div>

  <ul class="contact">
    <li>Kempton Vale</li>
    <li>Hobart, Tasmania 7030</li>
    <li>
      <svg viewBox="0 0 12 12"><path d="M2.5 1 L4.5 1 L5.3 3.5 L4 4.5 Q5 7 7.5 8 L8.5 6.7 L11 7.5 L11 9.5 Q10.5 11 9 11 Q1 10 1 3 Q1 1.5 2.5 1 Z" fill="#fff"/></svg>
      +61 412 885 107
    </li>
    <li>
      <svg viewBox="0 0 12 12"><rect x="0.7" y="2.2" width="10.6" height="7.6" fill="none" stroke="#fff" stroke-width="1.2"/><path d="M0.7 2.4 L6 6.6 L11.3 2.4" fill="none" stroke="#fff" stroke-width="1.2"/></svg>
      marklowry@pavemail.com.au
    </li>
    <li>
      <svg viewBox="0 0 12 12"><circle cx="6" cy="6" r="5" fill="none" stroke="#fff" stroke-width="1.1"/><ellipse cx="6" cy="6" rx="2.2" ry="5" fill="none" stroke="#fff" stroke-width="1"/><path d="M1 6 H11" stroke="#fff" stroke-width="1"/></svg>
      www.ashbypaving.com.au
    </li>
    <li><span class="abn-label">ABN</span> 27613048852</li>
  </ul>
</section>

<section class="card card-back" aria-label="Business card back">
  <div class="brand">
    <div class="brand-mark" aria-hidden="true"></div>
    <div class="brand-divider"></div>
    <div class="brand-text">
      <p class="brand-name">Ashby Paving Works</p>
      <div class="brand-rule"></div>
      <p class="brand-phone">0412885107</p>
    </div>
  </div>

  <div class="services">
    <p class="services-tagline">For all your concreting solutions</p>
    <ul class="services-list">
      <li>Excavation</li>
      <li>Exposed &amp; colour concrete</li>
      <li>House &amp; shed slabs</li>
      <li>Driveways</li>
      <li>Landing &amp; steps</li>
    </ul>
  </div>

  <p class="web">www.ashbypaving.com.au</p>
</section>

</body>
</html>
```